Website Redesign for Asset Management

We need a full redesign on the website for Velquist Asset Management. Velquist is an asset manager that manages both long - only products and alternative investments. We would like to see a clean and innovative website that showcases the products of the firm and the management of the firm.
www.velquist.example

Output should be in PSD and designer should have groups/layers for the developer to extract the imagesĀ 

Feel free to play with the colours as we are not stuck to current colours.

Target Market(s)

The target market are affluent individuals, pensions, foundations and endowments

Industry/Entity Type

Asset Management

Requirements
Must have
• We like the websites
www.dalbrenholt.example
www.kestrafund.example
DO LIKE
http://www.norvanta.example/#Home
http://www.dalbrenholt.example/who-we-are/principals.html
http://www.qlendry.example/default.aspx
http://www.kv3.example/
http://www.morvainpell.example/Home
https://www.halvorenfund.example/index.asp
http://www.ostrela.example/Home_Page.html
http://www.rdgulvo.example/#!contact/c16fm
http://www.pikemerefund.example/
http://www.varnelo.example/
https://www.quorvelpartners.example/
http://www.dxmrf.example/
http://www.fendrickco.example/

Don't Like
http://www.tellowayasset.example
http://klavin.example/
http://rmobrand.example/
http://www.tkwilder.example/operations_team.html

Also must have a section entitles Alternative Investments

```html
<!DOCTYPE html>
<html lang="en">
<head>
<meta charset="utf-8">
<title>Velquist Asset Management</title>
<link rel="stylesheet" href="https://fonts.googleapis.com/css2?family=Marcellus&display=swap">
<style>
  :root {
    --page-bg: #f2f2f2;
    --site-bg: #ffffff;
    --ink: #333333;
    --ink-soft: #6b6b6b;
    --rule: #cfcfcf;
    --tile-profil: #d9583a;
    --tile-process: #1fb8c3;
    --tile-solution: #0fa01f;
    --tile-news: #0a5cc2;
    --tile-contact: #c41d4f;
    --accent-red: #c62828;
    --photo-grey: linear-gradient(135deg, #c9ccd1, #8c939c);
    --photo-sketch: linear-gradient(135deg, #f4f4f4, #d7d3cf);
    --photo-warm: linear-gradient(135deg, #d9c4ae, #7d6a5a);
    --photo-light: linear-gradient(135deg, #e5ecf3, #a7b7c6);
    --photo-bulb: linear-gradient(135deg, #3a2a18, #e0a040);
    --photo-darts: linear-gradient(135deg, #1f3d8f, #0f1f4a);
    --photo-strategy: linear-gradient(135deg, #f2f2f2, #d63030);
  }
  * { box-sizing: border-box; margin: 0; padding: 0; }
  html, body { width: 1200px; height: 810px; overflow: hidden; }
  body {
    background: var(--page-bg);
    font-family: "Marcellus", serif;
    color: var(--ink);
    display: flex;
    align-items: center;
    justify-content: center;
  }
  .site {
    width: 1120px;
    height: 770px;
    background: var(--site-bg);
    padding: 0 35px;
    display: flex;
    flex-direction: column;
  }
  .site-header {
    display: flex;
    justify-content: space-between;
    align-items: center;
    height: 92px;
    border-bottom: 1px solid var(--rule);
  }
  .nav {
    display: flex;
    gap: 18px;
    list-style: none;
    font-size: 11px;
    letter-spacing: 0.04em;
    text-transform: uppercase;
    color: var(--ink-soft);
    white-space: nowrap;
  }
  .brand { text-align: center; padding: 0 16px; white-space: nowrap; }
  .brand-name { display: flex; align-items: center; justify-content: center; gap: 8px; font-size: 28px; color: var(--ink); }
  .brand-mark { width: 10px; height: 10px; background: var(--accent-red); }
  .brand-tagline { font-size: 11px; color: var(--ink-soft); margin-top: 2px; letter-spacing: 0.02em; }

  .tiles {
    margin-top: 24px;
    display: grid;
    grid-template-columns: repeat(6, 1fr);
    grid-template-rows: repeat(3, 145px);
    height: 435px;
  }
  .tile { position: relative; }
  .tile-label {
    position: absolute; left: 18px; top: 16px; right: 12px;
    color: #fff; font-size: 17px; letter-spacing: 0.06em; text-transform: uppercase; line-height: 1.25;
  }
  .tile--profil { background: var(--tile-profil); grid-column: 2; grid-row: 1; }
  .tile--process { background: var(--tile-process); grid-column: 5; grid-row: 1; }
  .tile--solution { background: var(--tile-solution); grid-column: 2; grid-row: 2; }
  .tile--news { background: var(--tile-news); grid-column: 4 / 6; grid-row: 2 / 4; }
  .tile--contact { background: var(--tile-contact); grid-column: 6; grid-row: 2; }
  .photo-sketch { background: var(--photo-sketch); grid-column: 1; grid-row: 1 / 3; }
  .photo-handshake { background: var(--photo-grey); grid-column: 3 / 5; grid-row: 1; }
  .photo-team { background: var(--photo-warm); grid-column: 6; grid-row: 1; }
  .photo-applause { background: var(--photo-light); grid-column: 3; grid-row: 2; }
  .photo-bulb { background: var(--photo-bulb); grid-column: 1 / 3; grid-row: 3; }
  .photo-darts { background: var(--photo-darts); grid-column: 3; grid-row: 3; }
  .photo-strategy { background: var(--photo-strategy); grid-column: 6; grid-row: 3; }

  .site-footer {
    margin-top: 28px;
    border-top: 1px solid var(--rule);
    padding-top: 22px;
    text-align: center;
    font-size: 12px;
    color: var(--ink-soft);
  }
  .footer-links { display: flex; justify-content: center; gap: 10px; list-style: none; white-space: nowrap; }
  .footer-links li + li::before { content: "·"; margin-right: 10px; }
  .copyright { margin-top: 8px; }
  .social { display: flex; justify-content: center; gap: 10px; margin-top: 14px; }
  .social span { width: 22px; height: 22px; border: 1px solid var(--ink-soft); border-radius: 50%; }
</style>
</head>
<body>
  <div class="site">
    <header class="site-header">
      <ul class="nav">
        <li>Home</li>
        <li>Profil</li>
        <li>Investment Process</li>
        <li>Investment Solution</li>
      </ul>
      <div class="brand">
        <div class="brand-name"><span class="brand-mark"></span>Velquist</div>
        <div class="brand-tagline">Growing Wealth Preserving Capital</div>
      </div>
      <ul class="nav">
        <li>Alternative Investments</li>
        <li>News &amp; Event</li>
        <li>Contact Us</li>
      </ul>
    </header>

    <main class="tiles">
      <div class="photo-sketch" role="img" aria-label="Hand sketching a solution diagram with arrows"></div>
      <a class="tile tile--profil"><span class="tile-label">Profil</span></a>
      <div class="photo-handshake" role="img" aria-label="Business handshake"></div>
      <a class="tile tile--process"><span class="tile-label">Investment<br>Process</span></a>
      <div class="photo-team" role="img" aria-label="Business team in discussion"></div>
      <a class="tile tile--solution"><span class="tile-label">Investment<br>Solution</span></a>
      <div class="photo-applause" role="img" aria-label="Colleagues clapping hands in an office"></div>
      <a class="tile tile--news"><span class="tile-label">News &amp; Event</span></a>
      <a class="tile tile--contact"><span class="tile-label">Contact Us</span></a>
      <div class="photo-bulb" role="img" aria-label="Hand holding a glowing light bulb"></div>
      <div class="photo-darts" role="img" aria-label="Darts on a target board"></div>
      <div class="photo-strategy" role="img" aria-label="Puzzle pieces spelling strategy"></div>
    </main>

    <footer class="site-footer">
      <ul class="footer-links">
        <li>Home</li>
        <li>Profil</li>
        <li>Investment process</li>
        <li>Investment solution</li>
        <li>Alternative investments</li>
        <li>Contact Us</li>
      </ul>
      <p class="copyright">© Velquist.example 2014. All Rights Reserved</p>
      <div class="social" aria-label="Social links">
        <span></span><span></span><span></span><span></span>
      </div>
    </footer>
  </div>
</body>
</html>
```